LINGERIE WEBSHOP - Velora casa

We are looking for design and layout design for our webshop. We are company that sells lingerie and other connected textile products liki payamas and etc..
Our website will have approx 500 different products within 2 main catogories Woman/Man) and approx. 10 subcategories
Here is what we expect form design:
-Color pallete should be black and white (if you wish you can add some accent color)
-we want to leave feeling to customers of good quality products towards to luxury
-UX should be simple. Feel free to suggest layout
-frontpage layout, product list layout, product description layout, blog layout
-responsive design, compatible with smartphone

Target Market(s)

woman buying for themself, man buying for woman

Industry/Entity Type

Lingerie

Logo Text

VELORA CASA

Number of Pages Required

4 page

Font styles to use
Sans Serif
Decorative

Requirements
Must have
• simple UX
Nice to have
• difference for sexy/luxury lingerie and daily/cozy lingerie
Should not have
• cheap feel, unreliable

```html
<!DOCTYPE html>
<html lang="en">
<head>
<meta charset="utf-8">
<title>Velora casa — Lingerie</title>
<link href="https://fonts.googleapis.com/css2?family=Marcellus&family=Montserrat:wght@400;500;600&display=swap" rel="stylesheet">
<style>
:root{
  --ink:#1c1b1d;
  --text:#555459;
  --muted:#8a8990;
  --line:#d9d9dc;
  --paper:#ffffff;
  --paper-soft:#f7f7f8;
  --hero-dark:#1a130e;
  --band-dark:#1c1814;
  --footer:#151417;
  --footer-text:#b9b8bd;
  --gold:#b0956a;
  --display:'Marcellus', serif;
  --body:'Montserrat', sans-serif;
}
*{box-sizing:border-box;margin:0;padding:0}
html,body{width:1200px;height:3288px;overflow:hidden}
body{position:relative;background:var(--paper);font-family:var(--body);color:var(--text)}
.abs{position:absolute}
.center-x{left:0;right:0;text-align:center}

/* Hero */
.hero{position:absolute;left:0;top:0;width:1200px;height:580px;
  background:
    radial-gradient(ellipse 150px 260px at 890px 300px, rgba(176,124,92,.85) 0%, rgba(120,80,56,.55) 45%, rgba(60,40,28,0) 100%),
    radial-gradient(ellipse 120px 180px at 1080px 200px, rgba(190,150,100,.35) 0%, rgba(0,0,0,0) 100%),
    linear-gradient(180deg, rgba(26,19,14,.2) 0%, rgba(26,19,14,0) 55%, rgba(100,74,52,.55) 75%, rgba(60,44,32,.7) 100%),
    radial-gradient(ellipse at 30% 45%, #4f3d2e 0%, #35281e 50%, var(--hero-dark) 100%)}
.search{left:83px;top:19px;width:203px;height:36px;border:1px solid rgba(255,255,255,.28);
  display:flex;align-items:center;justify-content:space-between;padding:0 10px;color:#e8e2dc;font-size:12px}
.logo{top:30px;font-family:var(--display);font-size:28px;color:#fff;letter-spacing:.5px}
.head-icons{top:26px;left:1000px;display:flex;gap:22px;align-items:center}
.hero-title{top:176px;left:170px;width:534px;text-align:center;color:#fff;font-family:var(--display)}
.hero-title .big{font-size:51px;letter-spacing:5px;line-height:1}
.hero-title .sub{font-size:38px;letter-spacing:10px;margin-top:8px;line-height:1}
.hero-rule{top:298px;left:424px;width:26px;height:2px;background:#fff}
.hero-copy{top:324px;left:170px;width:534px;text-align:center;color:#e3ddd6;font-size:14.5px;line-height:23px}
.btn-outline{display:flex;align-items:center;justify-content:center;border:1px solid;
  font-family:var(--body);letter-spacing:4px;text-transform:uppercase}
.hero-btn{top:406px;left:356px;width:161px;height:41px;color:#fff;border-color:rgba(255,255,255,.8);font-size:12px}

/* Promo cards */
.promo{top:647px;height:397px;width:500px}
.promo-man{left:83px;background:
  radial-gradient(ellipse 130px 170px at 250px 240px, rgba(70,66,72,.6), rgba(0,0,0,0) 100%),
  radial-gradient(ellipse 120px 90px at 230px 40px, rgba(30,40,60,.7), rgba(0,0,0,0) 100%),
  linear-gradient(160deg,#2a292d,#1f1e22 60%,#19181b)}
.promo-man .btn-outline{position:absolute;left:134px;top:179px;width:234px;height:41px;color:#fff;border-color:var(--gold);font-size:13px}
.promo-dress{left:616px;background:
  radial-gradient(ellipse 95px 150px at 320px 250px, rgba(236,238,240,.95) 0%, rgba(210,214,216,.6) 55%, rgba(0,0,0,0) 100%),
  radial-gradient(ellipse 70px 70px at 330px 95px, rgba(90,60,50,.8), rgba(0,0,0,0) 100%),
  radial-gradient(ellipse 90px 260px at 470px 200px, rgba(30,28,26,.85), rgba(0,0,0,0) 100%),
  linear-gradient(100deg,#1c2427 0%,#34434a 40%,#7b878c 65%,#aeb6b9 100%)}
.promo-dress .title{position:absolute;left:43px;top:57px;font-family:var(--display);font-size:31px;line-height:34px;color:#fff;letter-spacing:1px}
.promo-dress .from{position:absolute;left:45px;top:139px;color:#f1f1f1;font-size:14px;letter-spacing:1px}
.promo-dress .btn-outline{position:absolute;left:44px;top:184px;width:131px;height:32px;color:#fff;border-color:#fff;font-size:12px}

/* Section titles */
.section-title{font-family:var(--display);font-weight:400;font-size:29px;letter-spacing:5px;color:var(--ink)}

/* Product rows */
.products{left:83px;width:1032px;display:flex;justify-content:space-between}
.product{width:239px;text-align:center}
.product .photo{width:239px;height:257px}
.product .name{margin-top:15px;font-size:14.5px;color:var(--text);letter-spacing:.4px}
.product .price{margin-top:9px;font-size:15px;color:var(--ink)}
.product .btn-outline{margin:15px auto 0;width:148px;height:34px;color:var(--muted);border-color:#9d9ca2;font-size:10px}
.arrow-dot{width:36px;height:36px;border-radius:50%;background:#2a292c;display:flex;align-items:center;justify-content:center}

/* Testimonials */
.testimonials{left:0;top:1615px;width:1200px;height:429px;
  background:
    radial-gradient(ellipse 260px 200px at 930px 170px, rgba(90,74,60,.6), rgba(0,0,0,0) 100%),
    radial-gradient(ellipse 300px 200px at 200px 150px, rgba(70,58,48,.5), rgba(0,0,0,0) 100%),
    radial-gradient(ellipse at 55% 45%, #2f2822 0%, var(--band-dark) 60%, #13100d 100%)}
.avatars{top:1748px;display:flex;justify-content:center;align-items:center;gap:28px}
.avatar{border-radius:50%;background:radial-gradient(circle at 50% 40%,#b08a70,#5a4535)}
.avatar.dim{opacity:.45}
.quote{top:1832px;left:255px;width:690px;text-align:center;color:#ece7e2;font-size:14px;line-height:23.5px}
.quote-rule{top:1920px;left:589px;width:22px;height:2px;background:#fff}
.author{top:1941px;font-size:14px;font-weight:600;color:#fff}
.role{top:1969px;font-size:9px;color:#bdb6ad;letter-spacing:.3px}

/* New collection */
.new-band{left:0;top:2044px;width:1200px;height:568px;background:var(--paper-soft)}

/* Newsletter */
.news-copy{top:2746px;color:var(--muted);font-size:14px;line-height:22px}
.news-form{top:2823px;left:355px;display:flex;gap:8px}
.news-input{width:337px;height:43px;border:1px solid #e3e3e6;display:flex;align-items:center;padding-left:22px;font-size:12px;color:var(--muted)}
.news-btn{width:146px;height:43px;background:#2d2c30;color:#fff;display:flex;align-items:center;justify-content:center;font-size:11px;letter-spacing:4px}

/* Footer */
.footer{left:0;top:2953px;width:1200px;height:335px;background:var(--footer)}
.foot-col{top:3008px}
.foot-head{font-size:15px;color:#cfced3;letter-spacing:.8px}
.foot-links{margin-top:26px;list-style:none;font-size:13px;color:var(--footer-text)}
.foot-links li{height:31px}
.contact-row{display:flex;align-items:center;gap:10px;font-size:13.5px;color:var(--footer-text);height:39px}
.cards{display:flex;gap:13px;margin-top:34px}
.card{width:41px;height:25px;border-radius:3px;background:#e9e9ec}
.share{display:flex;align-items:center;gap:16px;margin-top:33px;font-size:15px;color:#cfced3;letter-spacing:.8px}
.share .dot{width:13px;height:13px;border-radius:50%;background:#cfced3}
.foot-rule{top:3230px;left:83px;width:1032px;height:1px;background:#2b2a2e}
.copyright{top:3248px;font-size:11px;color:#8d8c92}
</style>
</head>
<body>

<!-- Hero -->
<header class="hero" role="img" aria-label="Model in black lace lingerie on a leather sofa beside a lamp">
  <div class="abs search"><span>Search Here</span>
    <svg width="16" height="16" viewBox="0 0 16 16" fill="none" stroke="#fff" stroke-width="1.4"><circle cx="7" cy="7" r="5.5"/><path d="M11 11l4 4"/></svg>
  </div>
  <div class="abs center-x logo">VELORA CASA</div>
  <div class="abs head-icons">
    <svg width="18" height="20" viewBox="0 0 18 20" fill="none" stroke="#fff" stroke-width="1.4"><circle cx="9" cy="6" r="4.5"/><path d="M1.5 19c0-4.5 3.4-7 7.5-7s7.5 2.5 7.5 7"/></svg>
    <svg width="16" height="20" viewBox="0 0 16 20" fill="none" stroke="#fff" stroke-width="1.4"><path d="M2 6h12l-1 13H3z"/><path d="M5 6V4a3 3 0 0 1 6 0v2"/></svg>
    <svg width="24" height="14" viewBox="0 0 24 14" fill="none" stroke="#fff" stroke-width="1.4" style="margin-left:10px"><path d="M0 1h24M4 7h20M0 13h24"/></svg>
  </div>
  <div class="abs hero-title"><div class="big">BEST LINGERIE</div><div class="sub">COLLECTION</div></div>
  <div class="abs hero-rule"></div>
  <p class="abs hero-copy">Proin vitae neque sit amet massa facilisis posuere.<br>Sed facilisis auctor diam eu finibus.</p>
  <div class="abs btn-outline hero-btn">Shop now</div>
</header>

<!-- Promo cards -->
<section class="abs promo promo-man" role="img" aria-label="Man wearing checked pyjama trousers">
  <div class="btn-outline">Man collection</div>
</section>
<section class="abs promo promo-dress" role="img" aria-label="Model in white lace bodysuit by a mirror">
  <div class="title">BEAUTY<br>DRESSES</div>
  <div class="from">Starts from $100</div>
  <div class="btn-outline">Shop now</div>
</section>

<!-- Featured collections -->
<h2 class="abs center-x section-title" style="top:1106px">FEATURED COLLECTIONS</h2>
<div class="abs products" style="top:1177px">
  <div class="product"><div class="photo" role="img" aria-label="Model in black lace set" style="background:radial-gradient(ellipse 55px 120px at 120px 140px,#3a2f2c 0%,rgba(58,47,44,.4) 60%,rgba(0,0,0,0) 100%),radial-gradient(ellipse 70px 130px at 125px 120px,#d9b49a,rgba(0,0,0,0) 100%),linear-gradient(160deg,#d0b09a,#a98a74 60%,#8d7362)"></div><div class="name">Aliquam auctor</div><div class="price">$120</div><div class="btn-outline">Shop now</div></div>
  <div class="product"><div class="photo" role="img" aria-label="Model in red lace set" style="background:radial-gradient(ellipse 55px 100px at 120px 150px,#9c2a40 0%,rgba(156,42,64,.4) 55%,rgba(0,0,0,0) 100%),radial-gradient(ellipse 70px 130px at 120px 120px,#e2c0aa,rgba(0,0,0,0) 100%),linear-gradient(160deg,#d3d0cc,#aba39d)"></div><div class="name">Aliquam auctor</div><div class="price">$130</div><div class="btn-outline">Shop now</div></div>
  <div class="product"><div class="photo" role="img" aria-label="Model in black set with leather jacket" style="background:radial-gradient(ellipse 80px 120px at 120px 150px,#2a2222 0%,rgba(42,34,34,.5) 60%,rgba(0,0,0,0) 100%),radial-gradient(ellipse 70px 130px at 120px 110px,#dcb8a0,rgba(0,0,0,0) 100%),linear-gradient(160deg,#cfa88e,#8a6e5c)"></div><div class="name">Aliquam auctor</div><div class="price">$180</div><div class="btn-outline">Shop now</div></div>
  <div class="product"><div class="photo" role="img" aria-label="Model in mint lace set" style="background:radial-gradient(ellipse 55px 100px at 110px 140px,#a7ddd6 0%,rgba(167,221,214,.4) 55%,rgba(0,0,0,0) 100%),radial-gradient(ellipse 70px 130px at 110px 130px,#d8b59e,rgba(0,0,0,0) 100%),linear-gradient(160deg,#c4c1bd,#8e8984)"></div><div class="name">Aliquam auctor</div><div class="price">$190</div><div class="btn-outline">Shop now</div></div>
</div>
<div class="abs arrow-dot" style="left:63px;top:1287px"><svg width="10" height="12" viewBox="0 0 10 12" fill="none" stroke="#fff" stroke-width="1.5"><path d="M7 1L2 6l5 5"/></svg></div>
<div class="abs arrow-dot" style="left:1103px;top:1287px"><svg width="10" height="12" viewBox="0 0 10 12" fill="none" stroke="#fff" stroke-width="1.5"><path d="M3 1l5 5-5 5"/></svg></div>

<!-- Testimonials -->
<section class="abs testimonials" role="img" aria-label="Dark backdrop of lingerie and pearls"></section>
<h2 class="abs center-x section-title" style="top:1674px;color:#fff">CLIENT TESTIMONIALS</h2>
<div class="abs center-x avatars">
  <div class="avatar dim" role="img" aria-label="Client portrait" style="width:36px;height:36px"></div>
  <div class="avatar dim" role="img" aria-label="Client portrait" style="width:46px;height:46px"></div>
  <div class="avatar" role="img" aria-label="Client portrait" style="width:64px;height:64px"></div>
  <div class="avatar dim" role="img" aria-label="Client portrait" style="width:46px;height:46px"></div>
  <div class="avatar dim" role="img" aria-label="Client portrait" style="width:36px;height:36px"></div>
</div>
<svg class="abs" style="left:82px;top:1837px" width="28" height="16" viewBox="0 0 28 16" fill="none" stroke="#fff" stroke-width="1.5"><path d="M27 8H2M8 1L1 8l7 7"/></svg>
<svg class="abs" style="left:1089px;top:1837px" width="28" height="16" viewBox="0 0 28 16" fill="none" stroke="#fff" stroke-width="1.5"><path d="M1 8h25M20 1l7 7-7 7"/></svg>
<p class="abs quote">Quisque dictum ultricies sollicitudin. Nullam tellus risus, lobortis ut cursus sed, bibendum et ante. Ut auctor arcu turpis, id sagittis orci elementum venenatis. Quisque et porttitor nunc. Sed aliquet non dui nec venenatis. Suspendisse congue sed felis posuere placerat.</p>
<div class="abs quote-rule"></div>
<div class="abs center-x author">Mira Solen</div>
<div class="abs center-x role">NAM TEMPUS EUISMOD ELIT</div>

<!-- New collection -->
<section class="abs new-band"></section>
<h2 class="abs center-x section-title" style="top:2105px">NEW COLLECTION</h2>
<div class="abs products" style="top:2177px">
  <div class="product"><div class="photo" role="img" aria-label="Model in ivory lace set" style="background:radial-gradient(ellipse 45px 70px at 120px 150px,#eee6d8 0%,rgba(238,230,216,.5) 60%,rgba(0,0,0,0) 100%),radial-gradient(ellipse 60px 125px at 120px 130px,#e5c6b0,rgba(0,0,0,0) 100%),linear-gradient(180deg,#f1f1f2,#e6e6e8)"></div><div class="name">Aliquam auctor</div><div class="price">$120</div><div class="btn-outline">Shop now</div></div>
  <div class="product"><div class="photo" role="img" aria-label="Model in black strappy set" style="background:radial-gradient(ellipse 45px 80px at 120px 150px,#2b2627 0%,rgba(43,38,39,.4) 60%,rgba(0,0,0,0) 100%),radial-gradient(ellipse 60px 125px at 120px 130px,#ddb496,rgba(0,0,0,0) 100%),linear-gradient(180deg,#f1f1f2,#e6e6e8)"></div><div class="name">Aliquam auctor</div><div class="price">$130</div><div class="btn-outline">Shop now</div></div>
  <div class="product"><div class="photo" role="img" aria-label="Model in blush bra and robe" style="background:radial-gradient(ellipse 45px 70px at 120px 150px,#f1d9cc 0%,rgba(241,217,204,.5) 60%,rgba(0,0,0,0) 100%),radial-gradient(ellipse 65px 125px at 120px 130px,#c89a80,rgba(0,0,0,0) 100%),linear-gradient(180deg,#f1f1f2,#e6e6e8)"></div><div class="name">Aliquam auctor</div><div class="price">$180</div><div class="btn-outline">Shop now</div></div>
  <div class="product"><div class="photo" role="img" aria-label="Model in black lace bodysuit" style="background:radial-gradient(ellipse 50px 100px at 120px 160px,#1f1c1d 0%,rgba(31,28,29,.5) 60%,rgba(0,0,0,0) 100%),radial-gradient(ellipse 60px 125px at 120px 120px,#d4b09a,rgba(0,0,0,0) 100%),linear-gradient(180deg,#f1f1f2,#e6e6e8)"></div><div class="name">Aliquam auctor</div><div class="price">$190</div><div class="btn-outline">Shop now</div></div>
</div>
<div class="abs arrow-dot" style="left:63px;top:2285px"><svg width="10" height="12" viewBox="0 0 10 12" fill="none" stroke="#fff" stroke-width="1.5"><path d="M7 1L2 6l5 5"/></svg></div>
<div class="abs arrow-dot" style="left:1103px;top:2285px"><svg width="10" height="12" viewBox="0 0 10 12" fill="none" stroke="#fff" stroke-width="1.5"><path d="M3 1l5 5-5 5"/></svg></div>

<!-- Newsletter -->
<h2 class="abs center-x section-title" style="top:2690px">SUBSCRIBE OUR NEWSLETTER</h2>
<p class="abs center-x news-copy">In sollicitudin bibendum rhoncus. Nunc erat felis, accumsan sit<br>amet velit eget, vestibulum accumsan enim.</p>
<div class="abs news-form">
  <div class="news-input">Enter Your Email</div>
  <div class="news-btn">SUBSCRIBE</div>
</div>

<!-- Footer -->
<footer class="abs footer"></footer>
<div class="abs foot-col" style="left:84px">
  <div class="foot-head">OUR LINKS</div>
  <ul class="foot-links"><li>About</li><li>Products</li><li>Reviews</li><li>Contact</li></ul>
</div>
<div class="abs foot-col" style="left:303px">
  <div class="foot-head">MORE</div>
  <ul class="foot-links"><li>Terms &amp; Conditions</li><li>Privacy Policy</li><li>Sitemap</li></ul>
</div>
<div class="abs foot-col" style="left:589px">
  <div class="foot-head">CONTACT US</div>
  <div style="margin-top:22px">
    <div class="contact-row"><svg width="13" height="13" viewBox="0 0 24 24" fill="#cfced3"><path d="M6.6 10.8a15 15 0 0 0 6.6 6.6l2.2-2.2a1 1 0 0 1 1-.25 11.4 11.4 0 0 0 3.6.57 1 1 0 0 1 1 1V20a1 1 0 0 1-1 1A17 17 0 0 1 3 4a1 1 0 0 1 1-1h3.5a1 1 0 0 1 1 1c0 1.25.2 2.45.57 3.57a1 1 0 0 1-.25 1z"/></svg>0207 555 0148</div>
    <div class="contact-row"><svg width="13" height="10" viewBox="0 0 13 10" fill="none" stroke="#cfced3" stroke-width="1.2"><rect x=".6" y=".6" width="11.8" height="8.8"/><path d="M.6.6l5.9 5 5.9-5"/></svg>hello@veloracasa.com</div>
  </div>
</div>
<div class="abs foot-col" style="left:908px">
  <div class="foot-head">PAYMENT METHOD</div>
  <div class="cards">
    <div class="card" role="img" aria-label="Payment card"></div>
    <div class="card" role="img" aria-label="Payment card"></div>
    <div class="card" role="img" aria-label="Payment card"></div>
    <div class="card" role="img" aria-label="Payment card"></div>
  </div>
  <div class="share">SHARE WITH US <span class="dot" role="img" aria-label="Social link"></span><span class="dot" role="img" aria-label="Social link"></span></div>
</div>
<div class="abs foot-rule"></div>
<div class="abs center-x copyright">© Velora casa. All Rights Reserved</div>

</body>
</html>
```